Educational Construction Organization needs Flyer for Upcoming Forum

We need a SAVE THE DATE Flyer for our 2020 Ravteq Forum. We work with Architects, Engineers, Contractors and Owners in the design and construction industry. Our mission is to evolve the capital projects industry through sharing of knowledge for optimized leadership, delivery and performance. The final design should communicate the connection between these industry professionals, our mission, and the Forum theme and byline.
Updates

Need extra days to review

Target Market(s)

Design and construction industry.

Industry/Entity Type

Construction

Font styles to use
Sans Serif

Colors

Designer to choose colors to be used in the design.

Requirements
Must have
• Title, By-line, 3 key topics, Date and location. Design that implements the theme with graphic(s) (not just text).
• NEW TITLE: FUTURE PROOFING: Connecting the dots to make sense of the "SMART" City
• 3 Key Topics: Smart Cities, Smart Institutions, Smart Connections
• Date: April 1-3, 2020
• Location: San Antonio, TX
Nice to have
• Please review attached problem statement for a better understanding of what this Forum will focus on when designing your graphic for the flyer.

```html
<!DOCTYPE html>
<html lang="en">
<head>
<meta charset="utf-8">
<title>Future Proofing – 2020 Ravteq Forum</title>
<link rel="stylesheet" href="https://fonts.googleapis.com/css2?family=Montserrat:wght@400;500;700;800;900&display=swap">
<style>
  :root {
    --navy: #1f3f8f;
    --green: #8db241;
    --white: #ffffff;
    --grey: #5a5a5a;
    --sky-top: #4a3a6b;
    --sky-mid: #b0527a;
    --water: #2a3558;
  }
  * { margin: 0; padding: 0; box-sizing: border-box; }
  html, body { width: 848px; height: 1200px; overflow: hidden; background: var(--white); }
  body { font-family: "Montserrat", Arial, sans-serif; }
  .flyer { position: relative; width: 848px; height: 1200px; background: var(--white); overflow: hidden; }

  .skyline-photo {
    position: absolute; left: 0; top: 0; width: 848px; height: 314px;
    background: linear-gradient(180deg, var(--sky-top) 0%, #6b4a7e 35%, var(--sky-mid) 62%, #7a4a7a 75%, var(--water) 100%);
  }
  .title-tab {
    position: absolute; left: 142px; top: 176px; width: 566px; height: 160px;
    background: var(--white); border-radius: 70px 70px 0 0;
  }

  .headline {
    position: absolute; left: 210px; top: 210px;
    color: var(--navy); font-weight: 900; font-size: 77px; line-height: 66px; letter-spacing: -1px;
  }
  .byline {
    position: absolute; left: 210px; top: 362px;
    color: var(--green); font-weight: 500; font-size: 35px; line-height: 38px; letter-spacing: 0.2px;
  }
  .intro {
    position: absolute; left: 0; width: 848px; top: 556px; text-align: center;
    color: var(--navy); font-weight: 500; font-size: 17px; line-height: 23px;
  }

  .topics { position: absolute; top: 606px; left: 0; width: 848px; }
  .topic { position: absolute; width: 180px; margin-left: -90px; text-align: center; }
  .topic svg { display: block; margin: 0 auto; }
  .topic-label {
    margin-top: 12px; color: var(--navy); font-weight: 800; font-size: 20px; line-height: 25px;
  }

  .save-date {
    position: absolute; left: 91px; top: 796px; width: 668px; height: 210px;
    border: 5px solid var(--green); padding: 7px;
  }
  .save-date-inner { width: 100%; height: 100%; background: var(--green); position: relative; }
  .save-title {
    position: absolute; top: 32px; width: 100%; text-align: center;
    color: var(--white); font-weight: 900; font-size: 45px; letter-spacing: 0.5px;
  }
  .detail { position: absolute; top: 97px; display: flex; align-items: center; gap: 18px; }
  .detail-text { color: var(--white); font-weight: 700; font-size: 21px; line-height: 25px; }
  .detail-date { left: 114px; }
  .detail-place { left: 323px; }

  .org-mark { position: absolute; top: 1022px; left: 236px; display: flex; align-items: center; gap: 30px; height: 116px; }
  .org-dot { width: 116px; height: 116px; border-radius: 50%; background: var(--navy); flex: none; }
  .org-name { color: var(--grey); font-weight: 500; font-size: 58px; line-height: 60px; letter-spacing: -1px; }

  .web-band {
    position: absolute; left: 0; top: 1146px; width: 848px; height: 54px;
    background: var(--navy); color: var(--white); text-align: center;
    font-weight: 800; font-size: 18px; line-height: 54px; letter-spacing: 6px;
  }
</style>
</head>
<body>
<main class="flyer">
  <div class="skyline-photo" role="img" aria-label="Night city skyline with lit skyscrapers reflected in a river"></div>
  <div class="title-tab"></div>

  <h1 class="headline">FUTURE<br>PROOFING</h1>
  <p class="byline">CONNECTING THE DOTS<br>TO MAKE SENSE OF THE<br>"SMART" CITY</p>

  <p class="intro">2020 RAVTEQ FORUM EXPLORES HOW THE BUILT<br>ENVIRONMENT CONNECTS THE DOTS TO ACHIEVE</p>

  <section class="topics">
    <div class="topic" style="left:226px">
      <svg width="110" height="110" viewBox="0 0 110 110" aria-hidden="true">
        <circle cx="55" cy="55" r="55" fill="#1f3f8f"/>
        <path d="M22 80 H88 M26 80 V62 H34 V48 H42 V80 M42 56 H50 V38 H58 V80 M58 52 H66 V30 L72 36 V80 M72 58 H80 V80" fill="none" stroke="#fff" stroke-width="2.5" stroke-linejoin="round"/>
      </svg>
      <div class="topic-label">SMART<br>Cities</div>
    </div>
    <div class="topic" style="left:414px">
      <svg width="110" height="110" viewBox="0 0 110 110" aria-hidden="true">
        <circle cx="55" cy="55" r="55" fill="#1f3f8f"/>
        <g fill="none" stroke="#fff" stroke-width="2.5" stroke-linejoin="round">
          <path d="M24 82 H86 M30 82 V50 H42 M80 82 V50 H68 M42 82 V36 L55 28 L68 36 V82"/>
          <path d="M55 28 V18 H62 V22 H55"/>
          <rect x="48" y="42" width="6" height="6"/><rect x="57" y="42" width="6" height="6"/>
          <rect x="48" y="54" width="6" height="6"/><rect x="57" y="54" width="6" height="6"/>
          <path d="M48 82 V68 H62 V82"/>
          <rect x="33" y="58" width="5" height="6"/><rect x="72" y="58" width="5" height="6"/>
        </g>
      </svg>
      <div class="topic-label">SMART<br>Institutions</div>
    </div>
    <div class="topic" style="left:592px">
      <svg width="110" height="110" viewBox="0 0 110 110" aria-hidden="true">
        <circle cx="55" cy="55" r="55" fill="#1f3f8f"/>
        <g stroke="#fff" stroke-width="4" fill="#fff">
          <line x1="55" y1="55" x2="37" y2="33"/><line x1="55" y1="55" x2="72" y2="30"/>
          <line x1="55" y1="55" x2="82" y2="58"/><line x1="55" y1="55" x2="60" y2="82"/>
          <line x1="55" y1="55" x2="30" y2="64"/>
          <circle cx="55" cy="55" r="12" stroke="none"/>
          <circle cx="37" cy="33" r="7" stroke="none"/><circle cx="72" cy="30" r="6" stroke="none"/>
          <circle cx="82" cy="58" r="7" stroke="none"/><circle cx="60" cy="82" r="7" stroke="none"/>
          <circle cx="30" cy="64" r="6" stroke="none"/>
        </g>
      </svg>
      <div class="topic-label">SMART<br>Connections</div>
    </div>
  </section>

  <section class="save-date">
    <div class="save-date-inner">
      <h2 class="save-title">SAVE THE DATE</h2>
      <div class="detail detail-date">
        <svg width="58" height="60" viewBox="0 0 58 60" aria-hidden="true">
          <rect x="3" y="8" width="52" height="49" rx="5" fill="none" stroke="#fff" stroke-width="5"/>
          <rect x="3" y="8" width="52" height="14" fill="#fff"/>
          <rect x="12" y="1" width="6" height="14" rx="3" fill="#fff"/><rect x="40" y="1" width="6" height="14" rx="3" fill="#fff"/>
          <g fill="#fff">
            <rect x="12" y="30" width="8" height="7"/><rect x="25" y="30" width="8" height="7"/><rect x="38" y="30" width="8" height="7"/>
            <rect x="12" y="42" width="8" height="7"/><rect x="25" y="42" width="8" height="7"/><rect x="38" y="42" width="8" height="7"/>
          </g>
        </svg>
        <p class="detail-text">April 1-3,<br>2020</p>
      </div>
      <div class="detail detail-place">
        <svg width="44" height="62" viewBox="0 0 44 62" aria-hidden="true">
          <path d="M22 2 C10 2 2 11 2 22 C2 36 22 60 22 60 C22 60 42 36 42 22 C42 11 34 2 22 2 Z" fill="#fff"/>
          <circle cx="22" cy="21" r="7" fill="#8db241"/>
        </svg>
        <p class="detail-text">San Antonio,<br>TX</p>
      </div>
    </div>
  </section>

  <div class="org-mark">
    <div class="org-dot"></div>
    <div class="org-name">Ravteq</div>
  </div>

  <footer class="web-band">RAVTEQFORUM.ORG</footer>
</main>
</body>
</html>
```